New website for gluVista

We are looking to redesign our e-newsletter gluVista. This a monthly newsletter that publishes the latest research and product news in the diabetes field for people with diabetes. Our current website is here: www.gluvista-news.example.

The parameters are the new site must incorporate our logo, must use the same colors (variation in shade and adding some colors is fine, but the initial pallet should stay) and must be in 1024 by 768 px. It is crucially important that the font in the new design be easily readable (dark, well spaced). If it could be a layered PSD that would be ideal. We have attached 2 sketches of our own brainstorming for a potential lay-out for the home and a new issue page, but these are very rough and should not in any way limit the true designers out there.

We're envisioning a very polished, sophisticated looking magazine-esque site that presents a lot of information. When we were brainstorming for new site ideas we looked at major monthly publications such as the Harbor Ledger (www.harborledger.example) or Velvet Hour (www.vh-mag.example). Like these sites we would still like to feature much of our newest content on the front page, but in a manner that makes good use of space and feels uncluttered. Information needs to be clearly labeled and easy to find. In terms of the overall tone of the website, we do very much want it to be nice and elegant looking site, and one that is targeting a smart, engaged audience.
Updates

Reason: I didn't realize I'd made this due on a Sunday. Please take a couple of extra days everyone.

Industry/Entity Type

News

Requirements
Must have
• The logo. The same color scheme we currently use
Nice to have
• We like the idea of having a featured content box, of using hover buttons on top for our various sections, and potentially using a 3 column setup. However, we are not web designers, so the designer can use these suggestions at their discretion.

```html
<!DOCTYPE html>
<html lang="en">
<head>
<meta charset="utf-8">
<title>gluVista — research and product news for people with diabetes</title>
<link href="https://fonts.googleapis.com/css2?family=Arimo:wght@400;700&family=Libre+Baskerville&display=swap" rel="stylesheet">
<style>
  :root {
    --frame-brown: #4a2a1c;
    --ink: #1a1a1a;
    --heading-brown: #3b2418;
    --teal: #4c9e9b;
    --teal-dark: #2e7a76;
    --teal-deep: #1d4d4a;
    --teal-light: #8cc7c4;
    --mint: #d3ecea;
    --sidebar: #efedeb;
    --line: #d9d9d9;
    --placeholder: #c6c6c6;
    --white: #ffffff;
    --pdf-red: #d1232a;
  }
  * { box-sizing: border-box; margin: 0; padding: 0; }
  html, body { width: 983px; height: 1200px; overflow: hidden; }
  body { background: var(--frame-brown); font-family: "Arimo", Arial, sans-serif; color: var(--ink); }
  .stage { position: relative; width: 1024px; height: 1250px; transform: scale(0.96); transform-origin: 0 0; }
  .abs { position: absolute; }

  .page { left: 22px; top: 27px; width: 980px; height: 1185px; background: var(--white); }

  .brand { left: 112px; top: 52px; font-family: "Libre Baskerville", Georgia, serif; font-size: 54px; color: var(--heading-brown); letter-spacing: -1px; }
  .tagline { left: 39px; top: 137px; font-family: "Libre Baskerville", Georgia, serif; font-size: 15px; color: var(--heading-brown); }
  .size-btn { top: 84px; width: 41px; height: 40px; border: 1px solid #9a9a9a; border-radius: 4px; background: linear-gradient(#f4f4f4, #cfcfcf); font-size: 24px; color: #555; display: flex; align-items: center; justify-content: center; }

  .mainnav { left: 22px; top: 179px; width: 980px; height: 44px; background: linear-gradient(var(--teal-light), var(--teal) 55%, var(--teal-dark)); display: flex; }
  .mainnav a { color: var(--white); font-weight: 700; font-size: 12px; text-decoration: none; display: flex; align-items: center; justify-content: center; border-right: 1px solid rgba(255,255,255,.35); height: 44px; }
  .mainnav a.active { background: var(--teal-deep); }
  .search { left: 692px; top: 186px; width: 183px; height: 30px; background: var(--white); border-radius: 8px; font-size: 11px; color: var(--teal-deep); padding: 10px 0 0 14px; }
  .adv-search { left: 884px; top: 186px; width: 110px; height: 30px; background: linear-gradient(#ffffff, #e2e2e2); border-radius: 8px; font-size: 11px; color: #333; text-align: center; padding-top: 9px; }

  .subnav { left: 22px; top: 223px; width: 980px; height: 37px; background: linear-gradient(#ffffff, #e9f3f2); border-bottom: 1px solid var(--line); font-size: 11px; display: flex; }
  .subnav span { padding: 13px 12px 0 14px; border-right: 1px solid var(--line); }

  .sidebar { left: 752px; top: 260px; width: 250px; height: 952px; background: var(--sidebar); border-left: 1px solid var(--line); }

  .card { background: var(--white); border: 1px solid var(--line); border-radius: 8px; box-shadow: 0 2px 4px rgba(0,0,0,.12); background-image: linear-gradient(#fff 80%, #f3f3f3); }
  .feature-image { left: 36px; top: 288px; width: 428px; height: 248px; border: 1px solid #e6e6e6; border-radius: 8px; background: var(--white); color: #e3e3e3; font-size: 24px; display: flex; align-items: center; justify-content: center; }
  h2 { font-weight: 400; font-size: 20px; color: var(--heading-brown); }
  .body-text { font-size: 12px; line-height: 18px; color: var(--ink); }
  .thumb { width: 155px; height: 160px; border-radius: 8px; background: var(--placeholder); color: var(--white); font-size: 18px; display: flex; align-items: center; justify-content: center; }
  .more { font-size: 12px; font-weight: 700; color: var(--ink); }

  .dropdown { left: 128px; top: 260px; width: 197px; height: 158px; background: var(--mint); box-shadow: 0 2px 6px rgba(0,0,0,.25); display: grid; grid-template-columns: 91px 106px; grid-auto-rows: 30px; gap: 1px; padding: 1px 0; font-size: 11px; }
  .dropdown span { background: #d6eeec; outline: 1px solid #bfe0dd; display: flex; align-items: center; justify-content: center; }

  .join { left: 763px; top: 282px; width: 230px; height: 242px; background: linear-gradient(#8ccbc8, #4f9f9b); border: 1px solid #bfbfbf; }
  .join-title { left: 0; top: 24px; width: 230px; text-align: center; color: var(--white); font-size: 22px; line-height: 30px; text-shadow: 0 1px 2px rgba(0,0,0,.45); }
  .join-btn { left: 15px; top: 113px; width: 201px; height: 117px; border: 1px solid #cfe9e7; border-radius: 8px; background: linear-gradient(#5caaa6, #2d7d79); color: var(--white); font-size: 16px; line-height: 22px; text-align: center; padding-top: 62px; }

  .print { left: 763px; top: 542px; width: 230px; height: 122px; background: var(--white); border: 1px solid #bfbfbf; }
  .print-text { left: 8px; top: 40px; width: 128px; text-align: center; font-size: 17px; line-height: 24px; color: #2b2b2b; }

  .tabs { left: 762px; top: 682px; display: flex; font-size: 11px; text-align: center; line-height: 13px; }
  .tabs span { width: 67px; height: 41px; padding-top: 8px; background: var(--teal); color: #e8f5f4; border-left: 1px solid rgba(255,255,255,.5); }
  .tabs span.on { background: var(--white); color: #333; }
  .tab-panel { left: 762px; top: 722px; width: 232px; height: 189px; background: var(--white); border: 1px solid #d4d4d4; padding: 14px 10px 0 12px; }
  .tab-panel h3 { font-size: 11px; font-weight: 700; margin-bottom: 6px; }
  .tab-panel h3::before { content: "››"; font-weight: 400; margin-right: 6px; color: #555; }
  .tab-panel p { font-size: 10.5px; line-height: 18px; padding-left: 13px; margin-bottom: 16px; }

  .footer { left: 0; top: 1226px; width: 1024px; text-align: center; color: var(--white); font-size: 10px; }
</style>
</head>
<body>
<div class="stage">
  <div class="abs page"></div>

  <header>
    <div class="abs brand">gluVista</div>
    <div class="abs tagline">research and product news for people with diabetes</div>
    <div class="abs size-btn" style="left:895px">A</div>
    <div class="abs size-btn" style="left:946px">A</div>
  </header>

  <nav class="abs mainnav">
    <a href="#" style="width:88px">Home</a>
    <a href="#" class="active" style="width:88px">Issues</a>
    <a href="#" style="width:99px">Columns</a>
    <a href="#" style="width:85px">Topics</a>
    <a href="#" style="width:96px">About Us</a>
  </nav>
  <div class="abs search">Search
    <svg class="abs" style="left:158px;top:7px" width="16" height="16" viewBox="0 0 16 16"><circle cx="6" cy="6" r="4.5" fill="none" stroke="#444" stroke-width="2"/><line x1="9.5" y1="9.5" x2="14" y2="13" stroke="#444" stroke-width="2.5" stroke-linecap="round"/></svg>
  </div>
  <div class="abs adv-search">Advanced Search</div>

  <div class="abs subnav"><span>CURRENT ISSUE</span><span>ARCHIVES</span></div>

  <aside class="abs sidebar"></aside>

  <main>
    <section class="abs card" style="left:30px;top:284px;width:713px;height:257px"></section>
    <div class="abs feature-image" role="img" aria-label="Featured story photograph">FEATURED CONTENT IMAGE</div>
    <div class="abs" style="left:487px;top:296px;width:240px">
      <h2 style="margin-bottom:12px">Featured Content</h2>
      <p class="body-text" style="margin-bottom:13px">Lorem ipsum dolor siit amet consecutor. Lorem ipsum dolor siit amet consecutor. Lorem ipsum dolor siit amet consecutor. Lorem ipsum dolor siit amet consecutor.</p>
      <p class="body-text">Lorem ipsum dolor siit amet consecutor. Lorem ipsum dolor siit amet consecutor. Lorem ipsum dolor siit amet consecutor. Lorem ipsum dolor siit amet consecutor.</p>
    </div>

    <div class="abs dropdown">
      <span>2011</span><span>January</span>
      <span>2010</span><span>February</span>
      <span>2009</span><span>March</span>
      <span>2008</span><span>April</span>
      <span>2007</span><span>May</span>
    </div>

    <!-- column cards -->
    <article class="abs card" style="left:30px;top:557px;width:344px;height:197px">
      <div class="abs thumb" style="left:13px;top:17px" role="img" aria-label="Editor column photo">Image</div>
      <h2 class="abs" style="left:182px;top:14px">From the Editor</h2>
      <p class="abs body-text" style="left:183px;top:47px;width:150px">Lorem ipsum dolor siit amet consecutor. Lorem ipsum dolor siit amet consecutor. Lorem ipsum dolor siit amet consecutor.</p>
      <span class="abs more" style="left:256px;top:144px">Read More...</span>
    </article>
    <article class="abs card" style="left:399px;top:557px;width:344px;height:197px">
      <div class="abs thumb" style="left:14px;top:17px" role="img" aria-label="Learning Curve column photo">Image</div>
      <h2 class="abs" style="left:184px;top:14px">Learning Curve</h2>
      <p class="abs body-text" style="left:185px;top:47px;width:150px">Lorem ipsum dolor siit amet consecutor. Lorem ipsum dolor siit amet consecutor. Lorem ipsum dolor siit amet consecutor.</p>
      <span class="abs more" style="left:258px;top:144px">Read More...</span>
    </article>
    <article class="abs card" style="left:30px;top:772px;width:344px;height:198px">
      <div class="abs thumb" style="left:13px;top:17px" role="img" aria-label="Sum Musings column photo">Image</div>
      <h2 class="abs" style="left:182px;top:14px">Sum Musings</h2>
      <p class="abs body-text" style="left:183px;top:47px;width:150px">Lorem ipsum dolor siit amet consecutor. Lorem ipsum dolor siit amet consecutor. Lorem ipsum dolor siit amet consecutor.</p>
      <span class="abs more" style="left:256px;top:144px">Read More...</span>
    </article>
    <article class="abs card" style="left:399px;top:772px;width:344px;height:198px">
      <div class="abs thumb" style="left:14px;top:17px" role="img" aria-label="Trial Watch column photo">Image</div>
      <h2 class="abs" style="left:184px;top:14px">Trial Watch</h2>
      <p class="abs body-text" style="left:185px;top:64px;width:150px">Lorem ipsum dolor siit amet consecutor. Lorem ipsum dolor siit amet consecutor. Lorem ipsum dolor siit amet consecutor.</p>
      <span class="abs more" style="left:258px;top:161px">Read More...</span>
    </article>
    <article class="abs card" style="left:30px;top:987px;width:344px;height:198px">
      <div class="abs thumb" style="left:13px;top:17px" role="img" aria-label="Quotable Quotes column photo">Image</div>
      <h2 class="abs" style="left:182px;top:14px">Quotable Quotes</h2>
      <p class="abs body-text" style="left:183px;top:47px;width:150px">Lorem ipsum dolor siit amet consecutor. Lorem ipsum dolor siit amet consecutor. Lorem ipsum dolor siit amet consecutor.</p>
      <span class="abs more" style="left:256px;top:144px">Read More...</span>
    </article>
    <article class="abs card" style="left:399px;top:987px;width:344px;height:198px">
      <div class="abs thumb" style="left:14px;top:17px" role="img" aria-label="Finger Sticks column photo">Image</div>
      <h2 class="abs" style="left:184px;top:14px">Finger Sticks</h2>
      <p class="abs body-text" style="left:185px;top:47px;width:150px">Lorem ipsum dolor siit amet consecutor. Lorem ipsum dolor siit amet consecutor. Lorem ipsum dolor siit amet consecutor.</p>
      <span class="abs more" style="left:258px;top:144px">Read More...</span>
    </article>
  </main>

  <section class="abs join">
    <div class="abs join-title">Join the gluVista<br>community!</div>
    <div class="abs join-btn">Sign up for a free<br>subscription here</div>
    <svg class="abs" style="left:86px;top:122px" width="58" height="46" viewBox="0 0 58 46">
      <rect x="2" y="4" width="48" height="38" rx="3" fill="#fff" stroke="#9cb" stroke-width="1.5"/>
      <rect x="2" y="4" width="48" height="8" fill="#6fa8d6"/>
      <rect x="8" y="17" width="10" height="12" fill="#bcd"/>
      <line x1="22" y1="19" x2="42" y2="19" stroke="#999" stroke-width="2"/>
      <line x1="22" y1="25" x2="40" y2="25" stroke="#999" stroke-width="2"/>
      <line x1="8" y1="34" x2="36" y2="34" stroke="#999" stroke-width="2"/>
      <line x1="54" y1="8" x2="38" y2="32" stroke="#f0b429" stroke-width="5" stroke-linecap="round"/>
    </svg>
  </section>

  <section class="abs print">
    <div class="abs print-text">Print our latest<br>issue here</div>
    <svg class="abs" style="left:142px;top:10px" width="82" height="100" viewBox="0 0 82 100">
      <path d="M2 2 H58 L80 24 V98 H2 Z" fill="#fafafa" stroke="#cfcfcf" stroke-width="1.5"/>
      <path d="M58 2 V24 H80" fill="#e6e6e6" stroke="#cfcfcf" stroke-width="1.5"/>
      <rect x="2" y="76" width="78" height="20" fill="var(--pdf-red)"/>
    </svg>
  </section>

  <div class="abs tabs">
    <span class="on">Recently<br>Added</span>
    <span>Most<br>Popular</span>
    <span>Editors<br>Picks</span>
  </div>
  <div class="abs tab-panel">
    <h3>Article 1</h3>
    <p>Lorem ipsum dolor siit amet consecutor. Lorem ipsum dolor siit amet dolor.</p>
    <h3>Article 2</h3>
    <p>Lorem ipsum dolor siit amet consecutor. Lorem ipsum dolor siit amet dolor.</p>
    <span class="abs more" style="right:10px;top:166px">More...</span>
  </div>

  <footer class="abs footer">© 2011 gluVista®. All rights reserved.</footer>
</div>
</body>
</html>
```